Vara - Boutique Lawfirm providing legal advice to regulated financial institutions

I'm looking for a web page for my boutique law firm, specialized in providing legal advice to financial regulated institutions as well as non-financial regulated entities. The web page should have the technical capability to be in Spanish and English. Logo, color and typography according to specs provided. The web page should at least have the following (titles names may vary): 1. Homepage that communicates quickly and succinctly exactly what the law firm specializes in, grabs attention with eye-catching images and immediately establishes credibility 2. Our Firm; 3. Practice Area, 4. Resource Center, 5. Contact us, 6. Case Study. 7. Social Responsibility. The web page should also: -have the capability to add videos. -be owned and edited by our company. -be amicable with Quadra and LinkedIn. -SEO -adaptable to mobile version. PLEASE SEE WEB SITE REFERENCE IN NICE TO HAVE SECTION

Target Market(s)

Banks, financial institutions, lawyers

Industry/Entity Type

Financial

Coding

Coded - Design and coding required

Number of Pages Required

5+ page

Font styles to use
Serif

Requirements
Must have
• Contact Form
Social media links (Quadra and Linkedin)
Nice to have
• Link to Whatsapp number

see these web sites for
references
https://www.briefmarkt.com
https://www.quillnest.com
https://www.pemberdale.com/en/capabilities/services/financial-services/consulting

```html
<!DOCTYPE html>
<html lang="en">
<head>
<meta charset="utf-8">
<title>Vara Legal Services</title>
<link href="https://fonts.googleapis.com/css2?family=Lora:wght@400;600&family=Open+Sans:wght@400;600&display=swap" rel="stylesheet">
<style>
:root{
  --green:#2f9a77;
  --green-dark:#268064;
  --navy:#17304a;
  --ink:#1d2b36;
  --text:#5d6770;
  --grey-bg:#eef0f0;
  --line:#d9dddf;
  --white:#ffffff;
}
*{box-sizing:border-box;margin:0;padding:0}
html,body{width:1200px;height:3861px;overflow:hidden}
body{font-family:"Open Sans",Arial,sans-serif;color:var(--text);background:var(--white);position:relative}
.serif{font-family:"Lora",Georgia,serif}
a{text-decoration:none;color:inherit}
.abs{position:absolute}
.btn{position:absolute;background:var(--green);color:#fff;font-family:"Lora",Georgia,serif;font-weight:600;font-size:16px;display:flex;align-items:center;justify-content:center;letter-spacing:.3px}
.accent{color:var(--green)}

/* header */
.site-header{position:absolute;left:0;top:0;width:1200px;height:107px;background:#fff}
.brand{position:absolute;left:109px;top:18px;display:flex;align-items:center;gap:10px}
.brand-mark{width:14px;height:14px;background:var(--green)}
.brand-name{font-family:"Lora",Georgia,serif;font-size:46px;color:var(--green);line-height:1}
.brand-sub{position:absolute;left:111px;top:70px;font-size:11px;letter-spacing:7px;color:var(--green)}
.topbar{position:absolute;top:10px;right:112px;display:flex;align-items:center;gap:22px;font-family:"Lora",Georgia,serif;font-size:17px;color:var(--ink)}
.topbar .phone{display:flex;align-items:center;gap:8px}
.req{background:var(--green);color:#fff;padding:12px 12px;font-size:16px;font-weight:600}
.nav{position:absolute;top:70px;right:110px;display:flex;gap:18px;font-family:"Lora",Georgia,serif;font-size:17px;color:var(--ink)}
.nav .active{color:var(--green)}

/* hero */
.hero{position:absolute;left:0;top:107px;width:1200px;height:575px;background:linear-gradient(160deg,#1f5d6b 0%,#9ed4d8 35%,#e4f3f4 52%,#5fb1b6 72%,#164a5a 100%)}
.hero h1{position:absolute;top:100px;width:100%;text-align:center;font-family:"Lora",Georgia,serif;font-weight:400;font-size:88px;color:var(--navy)}
.hero p{position:absolute;top:218px;width:100%;text-align:center;font-size:22px;line-height:37px;color:var(--navy)}
.watch{position:absolute;left:479px;top:323px;width:241px;height:66px;border:1.5px solid var(--navy);display:flex;align-items:center;justify-content:center;gap:14px;font-family:"Lora",Georgia,serif;font-weight:600;font-size:20px;color:var(--navy)}

/* trusted */
.trusted-title{position:absolute;top:728px;width:100%;text-align:center;font-family:"Lora",Georgia,serif;font-weight:400;font-size:26px;color:var(--ink)}
.client{position:absolute;top:796px;width:183px;height:97px;border:1px solid var(--line);display:flex;align-items:center;justify-content:center;font-family:"Lora",Georgia,serif;font-size:26px;color:#9aa0a4}
.divider{position:absolute;left:111px;top:947px;width:978px;height:1px;background:var(--line)}

/* welcome */
.welcome h2{position:absolute;left:108px;top:994px;font-family:"Lora",Georgia,serif;font-weight:400;font-size:50px;line-height:56px;color:var(--ink)}
.welcome p{position:absolute;left:111px;width:530px;font-size:16.5px;line-height:31px}
.orb{position:absolute;left:684px;top:1020px;width:442px;height:442px;border-radius:50%;background:radial-gradient(circle,#8fd3bb 0%,#4f9ea3 45%,#2b4d6b 80%,rgba(255,255,255,0) 82%)}

/* solutions */
.solutions{position:absolute;left:0;top:1518px;width:1200px;height:584px;background:var(--grey-bg)}
.section-title{position:absolute;width:100%;text-align:center;font-family:"Lora",Georgia,serif;font-weight:400;font-size:50px;line-height:57px;color:var(--ink)}
.card{position:absolute;top:196px;width:306px;height:324px;background:#fff;text-align:center}
.card svg{margin-top:24px}
.card h3{font-family:"Lora",Georgia,serif;font-weight:400;font-size:25px;color:var(--ink);margin-top:14px}
.card p{font-size:16px;line-height:28px;margin:10px 18px 0}
.card .more{display:block;margin-top:12px;font-family:"Lora",Georgia,serif;font-size:16px;color:var(--green)}

/* focus */
.focus-col h3{position:absolute;top:2278px;font-family:"Lora",Georgia,serif;font-weight:400;font-size:33px;line-height:40px;color:var(--ink)}
.focus-col p{position:absolute;top:2380px;width:435px;font-size:16.5px;line-height:31.5px}
.scroll{position:absolute;width:12px;background:#d6d9db}
.scroll .thumb{position:absolute;left:0;width:12px;height:30px;background:#a9afb3}

/* resources */
.resources{position:absolute;left:0;top:2692px;width:1200px;height:586px;background:var(--grey-bg)}
.res-panel{position:absolute;left:111px;top:136px;width:601px;height:381px;background:#fff}
.res-item{position:absolute;width:240px}
.res-item .tag{font-size:14px;color:var(--green)}
.res-item h4{font-family:"Lora",Georgia,serif;font-weight:400;font-size:17px;line-height:26px;color:var(--ink);margin-top:8px}
.res-item.hl h4{color:var(--green)}
.res-item .date{font-size:13.5px;color:var(--green);margin-top:12px;display:flex;align-items:center;gap:6px}
.res-item .date span{color:#8a9297}
.res-feature{position:absolute;left:762px;top:136px;width:302px}
.res-img{width:302px;height:173px;background:linear-gradient(135deg,#e9e1d3,#b7c4cf 45%,#2f4d6b)}
.res-feature h4{font-family:"Lora",Georgia,serif;font-weight:400;font-size:20px;line-height:28px;color:var(--ink);margin-top:20px}
.res-feature .date{font-size:13.5px;color:#8a9297;margin-top:10px;display:flex;gap:6px;align-items:center}
.res-feature p{font-size:15px;line-height:24px;color:#8a9297;margin-top:14px}

/* contact */
.contact{position:absolute;left:0;top:3278px;width:1200px;height:583px;background:linear-gradient(180deg,#1c3c5a 0%,#17344f 60%,#132c44 100%);color:#fff}
.contact .section-title{color:#fff;top:44px}
.contact h5{position:absolute;font-weight:400;font-size:21px;color:#fff}
.field{position:absolute;background:#fff;border-radius:5px;font-size:15px;color:#666;padding:14px 15px}
.info{position:absolute;left:779px;display:flex;align-items:center;gap:15px;font-size:16px}
.ring{width:33px;height:33px;border-radius:50%;border:1px solid rgba(255,255,255,.7);display:flex;align-items:center;justify-content:center}
.social{position:absolute;width:33px;height:33px;border-radius:50%;border:1px solid rgba(255,255,255,.7);display:flex;align-items:center;justify-content:center;font-size:14px;font-weight:600;color:#fff}
.foot-line{position:absolute;left:111px;width:970px;height:1px;background:rgba(255,255,255,.35)}
.copyright{position:absolute;width:100%;text-align:center;font-size:15px;color:#fff}
</style>
</head>
<body>

<header class="site-header">
  <div class="brand"><span class="brand-name">Vara</span><span class="brand-mark"></span></div>
  <div class="brand-sub">LEGAL SERVICES</div>
  <div class="topbar">
    <span class="phone"><svg width="16" height="16" viewBox="0 0 16 16"><circle cx="8" cy="8" r="6.5" fill="none" stroke="#2f9a77" stroke-width="1.6"/><path d="M5.5 5.2c.4 2.4 2 4.3 4.6 5l.7-1.2-1.4-.8-.6.6C7.8 8.3 7.3 7.6 7 6.8l.6-.5-.7-1.5z" fill="#2f9a77"/></svg>1 555 014 2270</span>
    <span>Eng &#8964;</span>
    <span class="req">REQUEST ACCESS</span>
  </div>
  <nav class="nav">
    <a class="active">Home</a><a>Our Firm</a><a>Practice Area</a><a>Resource Center</a><a>Contact us</a><a>Case Study</a><a>Media</a>
  </nav>
</header>

<section class="hero" role="img" aria-label="City skyscrapers overlaid with glowing financial chart bars">
  <h1>Legal Services</h1>
  <p>We specialized in providing legal advice to financial regulated<br>institutions as well as non-financial regulated entities</p>
  <a class="watch"><svg width="38" height="38" viewBox="0 0 38 38"><circle cx="19" cy="19" r="17" fill="none" stroke="#17304a" stroke-width="1.6"/><path d="M15 12l11 7-11 7z" fill="#17304a"/></svg>WATCH VIDEO</a>
</section>

<h2 class="trusted-title">Trusted by some of the todays leading companies</h2>
<svg class="abs" style="left:48px;top:830px" width="20" height="30" viewBox="0 0 20 30"><path d="M15 3L4 15l11 12" fill="none" stroke="#666" stroke-width="2.5"/></svg>
<svg class="abs" style="left:1132px;top:830px" width="20" height="30" viewBox="0 0 20 30"><path d="M5 3l11 12L5 27" fill="none" stroke="#666" stroke-width="2.5"/></svg>
<div class="client" style="left:109px">Corvane</div>
<div class="client" style="left:307px">Corvane</div>
<div class="client" style="left:506px">Brisk</div>
<div class="client" style="left:704px">Corvane</div>
<div class="client" style="left:903px">Halden</div>
<div class="divider"></div>

<section class="welcome">
  <h2>Welcome to<br><span class="accent">Vara Legal Services</span></h2>
  <p style="top:1130px">Nemo enim ipsam voluptatem quia voluptas sit aspernatur aut odit aut fugit, sed quia consequuntur magn.</p>
  <p style="top:1223px">Dolores eos qui ratione volu ptatem sequi nesciunt. Neque porro qui squam est, qui dolorem ipsum quia dolor sit amet, consectetur, adip isci velit, sed quia non numquam eius modi tempora incidunt ut lab ore et dolore magnam aliquam qua.</p>
  <a class="btn" style="left:111px;top:1378px;width:140px;height:48px">READ MORE</a>
  <div class="orb" role="img" aria-label="Cluster of circles filled with financial imagery"></div>
</section>

<section class="solutions">
  <h2 class="section-title" style="top:46px">Our Complete Financial<br><span class="accent">Services Regulatory solution</span></h2>
  <div class="card" style="left:111px">
    <svg width="90" height="90" viewBox="0 0 90 90" fill="none" stroke="#17304a" stroke-width="2.2"><rect x="4" y="4" width="56" height="80"/><path d="M14 18h36M14 28h36M14 38h24M14 48h20"/><path d="M52 40l18-14 8 10-18 14z" stroke="#2f9a77"/><path d="M62 46l20 34" stroke="#2f9a77"/></svg>
    <h3>Legal</h3>
    <p>Ut enim ad minima veniam, quis nostrum exercitationem ullam corp oris suscipit laboriosa</p>
    <a class="more">READ MORE</a>
  </div>
  <div class="card" style="left:448px">
    <svg width="90" height="90" viewBox="0 0 90 90" fill="none" stroke="#17304a" stroke-width="2.2"><rect x="4" y="14" width="82" height="56"/><path d="M30 80h30M45 70v10"/><circle cx="24" cy="34" r="7"/><path d="M12 56c2-9 22-9 24 0"/><path d="M44 36h30M44 46h30M44 56h20"/><rect x="48" y="2" width="36" height="20" rx="3" fill="#fff" stroke="#2f9a77"/><circle cx="58" cy="12" r="2" stroke="#2f9a77"/><circle cx="66" cy="12" r="2" stroke="#2f9a77"/><circle cx="74" cy="12" r="2" stroke="#2f9a77"/></svg>
    <h3>Consulting</h3>
    <p>Ut enim ad minima veniam, quis nostrum exercitationem ullam corp oris suscipit laboriosa</p>
    <a class="more">READ MORE</a>
  </div>
  <div class="card" style="left:782px">
    <svg width="90" height="90" viewBox="0 0 90 90" fill="none" stroke="#17304a" stroke-width="2.2"><rect x="14" y="4" width="64" height="82"/><circle cx="32" cy="22" r="8"/><path d="M48 18h22M48 26h22"/><path d="M22 56l14-12 10 8 18-16" stroke="#2f9a77"/><path d="M26 76V64M38 76V58M50 76V60M62 76V54M20 78h52"/></svg>
    <h3>Managed Legal Services</h3>
    <p>Ut enim ad minima veniam, quis nostrum exercitationem ullam corp oris suscipit laboriosa</p>
    <a class="more">READ MORE</a>
  </div>
</section>

<section class="focus">
  <h2 class="section-title" style="top:2150px">Area of <span class="accent">Focus</span></h2>
  <div class="focus-col">
    <h3 style="left:109px">Financial Regulated<br>Institutions</h3>
    <p style="left:109px">Nemo enim ipsam voluptatem quia voluptas sit asperna tur aut odit aut fugit, sed quia consequuntur magni dolo res eos qui ratione voluptatem sequi nesciunt. Neque po rro quisquam est, qui dolor.</p>
    <a class="btn" style="left:111px;top:2533px;width:140px;height:48px">READ MORE</a>
  </div>
  <div class="scroll" style="left:568px;top:2252px;height:380px"><div class="thumb" style="top:158px"></div></div>
  <div class="focus-col">
    <h3 style="left:620px">Non-Financial Regulated<br>Entities</h3>
    <p style="left:619px">Nemo enim ipsam voluptatem quia voluptas sit asperna tur aut odit aut fugit, sed quia consequuntur magni dolo res eos qui ratione voluptatem sequi nesciunt. Neque po rro quisquam est, qui dolor.</p>
    <a class="btn" style="left:621px;top:2533px;width:140px;height:48px">READ MORE</a>
  </div>
  <div class="scroll" style="left:1078px;top:2252px;height:380px"><div class="thumb" style="top:158px"></div></div>
</section>

<section class="resources">
  <h2 class="section-title" style="top:46px">Resource <span class="accent">Center</span></h2>
  <div class="res-panel">
    <div class="res-item hl" style="left:40px;top:30px"><div class="tag">News</div><h4>Neque porro quisquam est qui dolorem ipsum quia dolor sit amet, consectetur.</h4><div class="date">&#9638; <span style="color:#2f9a77">02 October 2020</span></div></div>
    <div class="res-item" style="left:315px;top:30px"><div class="tag">Press Releases</div><h4>Neque porro quisquam est qui dolorem ipsum quia dolor sit amet, consectetur.</h4><div class="date">&#9638; <span>02 October 2020</span></div></div>
    <div class="res-item" style="left:40px;top:203px"><div class="tag">Insights</div><h4>Neque porro quisquam est qui dolorem ipsum quia dolor sit amet, consectetur.</h4><div class="date">&#9638; <span>02 October 2020</span></div></div>
    <div class="res-item" style="left:315px;top:203px"><div class="tag">News</div><h4>Neque porro quisquam est qui dolorem ipsum quia dolor sit amet, consectetur.</h4><div class="date">&#9638; <span>02 October 2020</span></div></div>
    <div class="scroll" style="left:599px;top:12px;height:360px"><div class="thumb" style="top:160px"></div></div>
  </div>
  <div class="res-feature">
    <div class="res-img" role="img" aria-label="Hand writing on documents beside a laptop with charts"></div>
    <h4>Neque porro quisquam est qui dolorem ipsum quia dolor sit amet, consectetur.</h4>
    <div class="date"><span style="color:#2f9a77">&#9638;</span> 02 October 2020</div>
    <p>Ut enim ad minima veniam, quis nostrum exercitationem ullam corporisqua</p>
  </div>
  <div class="scroll" style="left:1078px;top:148px;height:358px"><div class="thumb" style="top:160px"></div></div>
</section>

<section class="contact" role="region" aria-label="Contact">
  <h2 class="section-title serif">Contact <span style="color:#3fae88">Us</span></h2>
  <h5 style="left:110px;top:136px">Request Access</h5>
  <div class="field" style="left:111px;top:190px;width:298px;height:45px">Name :</div>
  <div class="field" style="left:417px;top:190px;width:298px;height:45px">Phone no :</div>
  <div class="field" style="left:111px;top:250px;width:604px;height:45px">Email :</div>
  <div class="field" style="left:111px;top:310px;width:604px;height:84px">Message :</div>
  <a class="btn" style="left:597px;top:409px;width:118px;height:48px;font-family:'Open Sans',Arial,sans-serif;font-size:17px">SUBMIT</a>
  <h5 style="left:778px;top:136px">Contact Information</h5>
  <div class="info" style="top:187px"><span class="ring"><svg width="14" height="14" viewBox="0 0 16 16"><circle cx="8" cy="8" r="6.5" fill="none" stroke="#fff" stroke-width="1.5"/><path d="M5.5 5.2c.4 2.4 2 4.3 4.6 5l.7-1.2-1.4-.8-.6.6C7.8 8.3 7.3 7.6 7 6.8l.6-.5-.7-1.5z" fill="#fff"/></svg></span>1 555 014 2270</div>
  <div class="info" style="top:252px"><span class="ring"><svg width="14" height="11" viewBox="0 0 14 11"><rect x="0" y="0" width="14" height="11" fill="#fff"/><path d="M0 0l7 6 7-6" fill="none" stroke="#17344f" stroke-width="1.4"/></svg></span>info@varalegalservices.com</div>
  <h5 style="left:778px;top:310px">Social Media</h5>
  <a class="social" style="left:776px;top:352px" aria-label="Pintle">P</a>
  <a class="social" style="left:823px;top:352px" aria-label="Kestro">K</a>
  <a class="social" style="left:869px;top:352px" aria-label="Quadra">Q</a>
  <div class="foot-line" style="top:497px"></div>
  <p class="copyright" style="top:528px">Copyright © 2020, Vara Legal services. All rights reserved.</p>
  <svg class="abs" style="left:1062px;top:526px" width="28" height="18" viewBox="0 0 28 18"><path d="M2 16L14 4l12 12" fill="none" stroke="#fff" stroke-width="3"/></svg>
</section>

</body>
</html>
```